Flaschenhalskarte für Weihnachten
korkwerk
Hat alles super geklappt - die Entscheidung für ein Design war schwer.
Zielgruppe
Wir beschäftigen uns mit dem Thema Wein und haben zur Informationen über Wein eine Flaschenhalskarte entwickelt. Diese Karte wollen wir nun Winzern und Händlern als Weihnachtsgrußkarte anbieten.
Aufgabenstellung
Es soll ein modernes und ansprechendes Design werden. Die Stanzlinien der Karte (Ausschnitt für den Flaschenhals und abfallender Rand) müssen berücksichtigt werden. Es können 2 Varianten angeboten werden - einmal die die ganze Länge, die Karte wird dann umgeklappt. Einmal nur bis zur Stanzlinie in der Mitte.
Die bisherigen Varianten der Karte findet man unter
http://korkanhaenger-muster.de/private-geniesser.html
Es dürfen auch Vorschläge für die Verpackung (einzeln und 10 Karten) gemacht werden.

```html
<!DOCTYPE html>
<html lang="de">
<head>
<meta charset="utf-8">
<title>Flaschenhalskarte Weihnachten</title>
<link rel="stylesheet" href="https://fonts.googleapis.com/css2?family=Cinzel:wght@400&family=Roboto+Slab:wght@400;800&family=PT+Sans+Narrow&display=swap">
<style>
  :root {
    --teal: #1a9e8f;
    --teal-dark: #0f8778;
    --teal-light: #27ab9c;
    --ink: #ffffff;
    --cutline: #2b3b3a;
    --page: #ffffff;
  }
  html, body {
    margin: 0;
    padding: 0;
    width: 1200px;
    height: 4500px;
    overflow: hidden;
    background: var(--page);
  }
  .neck-card {
    position: relative;
    width: 1200px;
    height: 4500px;
  }
  .card-shape, .neck-cutout, .fold-line, .divider {
    position: absolute;
    left: 0;
    top: 0;
  }
  .ornament {
    position: absolute;
    left: 230px;
    width: 740px;
    height: 80px;
    border-radius: 40px;
    background: linear-gradient(90deg, rgba(255,255,255,0.15), rgba(255,255,255,0.55) 50%, rgba(255,255,255,0.15));
  }
  .ornament--top { top: 1265px; }
  .ornament--mid { top: 2585px; }
  .ornament--quote-top { top: 3020px; }
  .ornament--quote-bottom { top: 3755px; }

  .greeting-line {
    position: absolute;
    left: 0;
    width: 1200px;
    margin: 0;
    text-align: center;
    color: var(--ink);
    white-space: nowrap;
  }
  .greeting-intro {
    top: 1405px;
    height: 100px;
    font-family: "Cinzel", serif;
    font-size: 74px;
    line-height: 100px;
    letter-spacing: 1px;
  }
  .greeting-main {
    font-family: "Roboto Slab", "Rockwell", serif;
    font-weight: 800;
  }
  .greeting-main span {
    display: block;
    transform: scaleX(0.82);
  }
  .greeting-main--christmas {
    top: 1600px;
    font-size: 124px;
    line-height: 135px;
  }
  .greeting-amp {
    top: 1885px;
    font-family: "Cinzel", serif;
    font-size: 40px;
    line-height: 46px;
  }
  .greeting-main--newyear {
    top: 1953px;
    font-size: 96px;
    line-height: 95px;
  }
  .greeting-year {
    top: 2250px;
    font-family: "Roboto Slab", "Rockwell", serif;
    font-weight: 400;
    font-size: 265px;
    line-height: 300px;
    letter-spacing: 6px;
  }
  .quote {
    position: absolute;
    left: 0;
    top: 3253px;
    width: 1200px;
    margin: 0;
    text-align: center;
    color: var(--ink);
    font-family: "PT Sans Narrow", sans-serif;
    font-size: 56px;
    line-height: 82px;
  }
  .quote-author {
    display: block;
    margin-top: 135px;
    font-size: 42px;
    line-height: 50px;
    font-style: normal;
  }
</style>
</head>
<body>
<main class="neck-card">
  <svg class="card-shape" width="1200" height="4500" viewBox="0 0 1200 4500" aria-hidden="true">
    <defs>
      <radialGradient id="cardTone" cx="50%" cy="45%" r="75%">
        <stop offset="0" stop-color="#27ab9c"/>
        <stop offset="0.7" stop-color="#1a9e8f"/>
        <stop offset="1" stop-color="#0f8778"/>
      </radialGradient>
    </defs>
    <path fill="url(#cardTone)" stroke="#2b3b3a" stroke-width="2"
      d="M77,24 H1123 V4335 H985 A32 32 0 1 0 935,4385 L915,4468 Q910,4485 892,4485 H308 Q290,4485 285,4468 L265,4385 A32 32 0 1 0 215,4335 H77 Z"/>
  </svg>

  <svg class="neck-cutout" width="1200" height="4500" viewBox="0 0 1200 4500" aria-hidden="true">
    <path fill="none" stroke="#2b3b3a" stroke-width="3"
      d="M290,1140 Q275,1165 300,1165 Q320,1160 315,1130 Q300,1000 330,880 Q370,740 360,620 Q350,510 440,480 Q520,430 600,425 Q680,430 760,480 Q850,510 840,620 Q830,740 870,880 Q900,1000 885,1130 Q880,1160 900,1165 Q925,1165 910,1140"/>
  </svg>

  <svg class="fold-line" width="1200" height="4500" viewBox="0 0 1200 4500" aria-hidden="true">
    <line x1="77" y1="2751" x2="1123" y2="2751" stroke="#0f8778" stroke-width="3"/>
  </svg>

  <div class="ornament ornament--top" role="img" aria-label="Verschnörkeltes weißes Ornament"></div>

  <p class="greeting-line greeting-intro">WIR WÜNSCHEN</p>

  <svg class="divider" width="1200" height="4500" viewBox="0 0 1200 4500" aria-hidden="true">
    <g stroke="#ffffff" stroke-width="14" stroke-dasharray="6 6">
      <line x1="257" y1="1551" x2="557" y2="1551"/>
      <line x1="629" y1="1551" x2="943" y2="1551"/>
      <line x1="257" y1="1908" x2="557" y2="1908"/>
      <line x1="643" y1="1908" x2="943" y2="1908"/>
    </g>
    <g fill="#ffffff">
      <line x1="257" y1="2256" x2="943" y2="2256" stroke="#ffffff" stroke-width="4"/>
      <circle cx="257" cy="2256" r="9"/>
      <circle cx="943" cy="2256" r="9"/>
    </g>
  </svg>

  <h1 class="greeting-line greeting-main greeting-main--christmas"><span>FROHE</span><span>WEIHNACHTEN</span></h1>
  <p class="greeting-line greeting-amp">&amp;</p>
  <h2 class="greeting-line greeting-main greeting-main--newyear"><span>EIN</span><span>GLÜCKLICHES</span><span>NEUES JAHR</span></h2>
  <p class="greeting-line greeting-year">2018</p>

  <div class="ornament ornament--mid" role="img" aria-label="Verschnörkeltes weißes Ornament"></div>
  <div class="ornament ornament--quote-top" role="img" aria-label="Verschnörkeltes weißes Ornament"></div>

  <blockquote class="quote">
    Die Geburt Jesu in Bethlehem ist<br>
    keine einmalige Geschichte, sondern<br>
    ein Geschenk, das immer bleibt.
    <cite class="quote-author">Matthias Lorenz</cite>
  </blockquote>

  <div class="ornament ornament--quote-bottom" role="img" aria-label="Verschnörkeltes weißes Ornament"></div>
</main>
</body>
</html>
```